brochure for payroll services

we need a brochure design for our new payroll services- either to be send to prospect as an email attachment or print. see attached on content required.
our corporate colour is orange . the design should communicate trust ,and reliability with a breadth of fresh air.

```html
<!DOCTYPE html>
<html lang="en">
<head>
<meta charset="utf-8">
<title>Caldera Payroll Services – Trifold Brochure</title>
<link rel="stylesheet" href="https://fonts.googleapis.com/css2?family=Cabin:wght@400;500;600;700&family=Marcellus&display=swap">
<style>
  :root {
    --brand-orange: #e2690f;
    --brand-orange-deep: #c95a0a;
    --ink: #1d1d1d;
    --ink-soft: #3a3a3a;
    --bar-grey: #5c5c5c;
    --paper: #ffffff;
    --cover-paper: #eceeef;
    --message-paper: #f5f3ef;
    --stage: #f1f0ee;
    --sky-blue: #a9c8e6;
  }

  * { box-sizing: border-box; margin: 0; padding: 0; }

  html, body {
    width: 1200px;
    height: 798px;
    overflow: hidden;
  }

  body {
    position: relative;
    background: var(--stage);
    font-family: "Cabin", "Gill Sans", sans-serif;
    color: var(--ink);
  }

  .format-label {
    position: absolute;
    left: 45px;
    top: 38px;
    font-size: 20px;
    font-weight: 500;
    color: var(--ink);
  }

  .panel {
    position: absolute;
    top: 86px;
    width: 270px;
    height: 625px;
    overflow: hidden;
  }

  /* ---------- Front cover ---------- */
  .cover {
    left: 45px;
    background: linear-gradient(160deg, #f4f5f6 0%, var(--cover-paper) 60%, #dfe2e4 100%);
    box-shadow: 0 2px 6px rgba(0,0,0,0.15);
  }

  .cover-brand {
    position: absolute;
    left: 28px;
    top: 58px;
    display: flex;
    align-items: center;
    gap: 12px;
  }

  .brand-square {
    width: 30px;
    height: 30px;
    background: var(--brand-orange);
  }

  .brand-name {
    font-size: 44px;
    font-weight: 500;
    color: var(--ink);
    letter-spacing: 0.5px;
  }

  .cover-visual {
    position: absolute;
    left: 0;
    top: 170px;
    width: 270px;
    height: 230px;
    background:
      radial-gradient(ellipse at 45% 45%, rgba(120,160,200,0.55) 0%, rgba(160,185,205,0.35) 40%, rgba(236,238,239,0) 75%),
      linear-gradient(180deg, rgba(236,238,239,0) 0%, rgba(150,170,190,0.3) 50%, rgba(236,238,239,0) 100%);
  }

  .cover-tagline {
    position: absolute;
    left: 28px;
    top: 425px;
    width: 230px;
  }

  .cover-service {
    font-size: 21px;
    font-weight: 700;
    color: var(--ink);
  }

  .cover-rule {
    height: 7px;
    background: var(--bar-grey);
    margin: 6px 0 4px;
  }

  .cover-trust {
    font-size: 60px;
    line-height: 1;
    font-weight: 400;
  }

  .cover-values {
    font-size: 27px;
    line-height: 1.1;
    font-weight: 400;
  }

  .cover-values.large { font-size: 35px; }

  /* ---------- Inside spread ---------- */
  .spread {
    position: absolute;
    left: 345px;
    top: 86px;
    width: 810px;
    height: 625px;
    box-shadow: 0 2px 6px rgba(0,0,0,0.15);
  }

  .spread .panel { top: 0; }

  .intro-panel {
    left: 0;
    background: linear-gradient(170deg, var(--paper) 0%, #f6f6f6 100%);
  }

  .section-band {
    position: absolute;
    left: 22px;
    top: 34px;
    width: 248px;
    height: 34px;
    background: var(--brand-orange);
    color: var(--paper);
    font-weight: 700;
    font-size: 16px;
    line-height: 34px;
    padding-left: 12px;
    letter-spacing: 0.3px;
  }

  .intro-copy {
    position: absolute;
    left: 24px;
    top: 90px;
    width: 228px;
    font-size: 12px;
    line-height: 1.4;
    color: var(--ink-soft);
  }

  .drop-cap {
    float: left;
    font-size: 52px;
    line-height: 0.85;
    color: var(--brand-orange);
    margin: 2px 6px 0 0;
  }

  .advantages {
    position: absolute;
    left: 24px;
    top: 232px;
    width: 228px;
  }

  .advantages-title {
    font-size: 14px;
    font-weight: 700;
    margin-bottom: 10px;
  }

  .advantages-list { list-style: none; }

  .advantages-list li {
    position: relative;
    padding-left: 16px;
    font-size: 12px;
    line-height: 1.35;
    color: var(--ink-soft);
    margin-bottom: 8px;
  }

  .advantages-list li::before {
    content: "";
    position: absolute;
    left: 3px;
    top: 5px;
    width: 5px;
    height: 5px;
    border-radius: 50%;
    background: var(--brand-orange);
  }

  .scope-panel {
    left: 270px;
    background: linear-gradient(170deg, #f8f8f8 0%, var(--paper) 100%);
  }

  .scope-title {
    position: absolute;
    left: 20px;
    top: 38px;
    font-size: 18px;
    font-weight: 700;
    color: var(--brand-orange);
    text-transform: uppercase;
  }

  .scope-intro {
    position: absolute;
    left: 20px;
    top: 70px;
    font-size: 12px;
    color: var(--ink-soft);
  }

  .scope-list {
    position: absolute;
    left: 38px;
    top: 100px;
    width: 215px;
    font-size: 12px;
    font-weight: 700;
    color: var(--ink);
  }

  .scope-list li {
    margin-bottom: 20px;
    padding-left: 8px;
  }

  .scope-visual {
    position: absolute;
    left: 0;
    top: 390px;
    width: 270px;
    height: 170px;
    background: radial-gradient(ellipse at 55% 50%, rgba(130,175,225,0.7) 0%, rgba(169,200,230,0.4) 45%, rgba(255,255,255,0) 75%);
  }

  .web-address {
    position: absolute;
    left: 20px;
    bottom: 28px;
    font-size: 18px;
    font-weight: 700;
    letter-spacing: 3px;
    color: var(--ink);
  }

  /* ---------- Orange flap ---------- */
  .flap-panel {
    left: 540px;
    background: linear-gradient(180deg, var(--brand-orange) 0%, var(--brand-orange-deep) 100%);
  }

  .flap-photo {
    position: absolute;
    left: 22px;
    top: 56px;
    width: 226px;
    height: 500px;
    background: linear-gradient(180deg, rgba(50,45,42,0.85) 0%, rgba(60,52,46,0.7) 55%, rgba(235,190,160,0.55) 80%, rgba(226,105,15,0) 100%);
  }

  .flap-message {
    position: absolute;
    left: 36px;
    top: 72px;
    width: 198px;
    padding: 10px 0 12px;
    background: var(--message-paper);
    font-family: "Marcellus", "Trajan Pro", serif;
    text-align: center;
    line-height: 1.02;
  }

  .message-lead { font-size: 44px; color: var(--brand-orange); }
  .message-sub { font-size: 27px; color: var(--brand-orange); }
  .message-small { font-size: 19px; color: var(--brand-orange); margin-top: 6px; }
  .message-focus { font-size: 27px; color: var(--ink); }
  .message-core { font-size: 21px; color: var(--brand-orange); }
  .message-end { font-size: 23px; color: var(--ink); }
</style>
</head>
<body>
  <div class="format-label">8.5″x11″ Trifold brochure</div>

  <section class="panel cover" aria-label="Front cover">
    <div class="cover-brand">
      <span class="brand-square"></span>
      <span class="brand-name">Caldera</span>
    </div>
    <div class="cover-visual" role="img" aria-label="Abstract blue-grey photo of modern glass architecture"></div>
    <div class="cover-tagline">
      <p class="cover-service">Payroll Services</p>
      <div class="cover-rule"></div>
      <p class="cover-trust">TRUST,</p>
      <p class="cover-values">RELIABILITY &amp;</p>
      <p class="cover-values large">EFFICIENCY</p>
    </div>
  </section>

  <div class="spread" aria-label="Inside spread">
    <section class="panel intro-panel">
      <h2 class="section-band">PEACE OF MIND FOR YOU</h2>
      <p class="intro-copy"><span class="drop-cap">S</span>o that you will not be distracted by technology selection, implementation and maintenance, attracting and retaining expertise and dedicated resources, keeping track of changes in regulations and potential conflict of interests within (knowing the salary and benefits for all).</p>
      <div class="advantages">
        <h3 class="advantages-title">Our advantages</h3>
        <ul class="advantages-list">
          <li>Project management and methodology to ensure seamless transition and sustainable delivery</li>
          <li>Domain knowledge in payroll, accounting &amp; finance and tax</li>
          <li>Robust technology platform for automation, control and visibility</li>
          <li>Proven delivery expertise and experience to provide reliable and trusted services</li>
        </ul>
      </div>
    </section>

    <section class="panel scope-panel">
      <h2 class="scope-title">Scope of services</h2>
      <p class="scope-intro">The scope covers the following services:</p>
      <ol class="scope-list">
        <li>Payroll processing</li>
        <li>Tax filing</li>
        <li>Benefits administration</li>
        <li>Leave tracking</li>
        <li>Payslip delivery</li>
        <li>Year-end reports</li>
        <li>Audit support</li>
        <li>Helpdesk</li>
      </ol>
      <div class="scope-visual" role="img" aria-label="Soft blue world map illustration"></div>
      <p class="web-address">www.caldera-pay.biz</p>
    </section>

    <section class="panel flap-panel">
      <div class="flap-photo" role="img" aria-label="Photo of a hand touching a tablet screen"></div>
      <div class="flap-message">
        <p class="message-lead">Peace</p>
        <p class="message-sub">OF MIND</p>
        <p class="message-lead">for you</p>
        <p class="message-small">TO ALLOW YOU</p>
        <p class="message-focus">TO FOCUS</p>
        <p class="message-core">on your core</p>
        <p class="message-end">ACTIVITIES</p>
      </div>
    </section>
  </div>
</body>
</html>
```